Exam room posters

Hi Tomo. I uploaded 2 files.
A) Let's start with COVID-19..
1. Please remove the person, descriptions and headline (preferred...) of the left half of the page.
2. Keep the PWR logo in the bottom.
3. Now change the orientation of the page. Means you have to shrink the COVID... headline in the top to make it fit .
4. The 2 items at the bottom, blue "PWR" logo and yellow "pwr-health.example.." remain at the bottom.
Please send that.
B) On the green document "Droplet..."
1. Please delete entire sentence at the bottom "Remove face protection before room exit". and send back to me.

Not sure how to add another project as I have paid for 6 designs. Can you help? Thank you!

```html
<!DOCTYPE html>
<html lang="en">
<head>
<meta charset="utf-8">
<title>Droplet Precautions</title>
<link rel="stylesheet" href="https://fonts.googleapis.com/css2?family=Fira+Sans+Extra+Condensed:wght@600;700&family=Arimo:wght@700&family=Nunito+Sans:wght@400;800&display=swap">
<style>
  :root {
    --page: #ffffff;
    --panel-green: #3a5a2b;
    --stop-red: #e41e26;
    --white: #ffffff;
    --headline-yellow: #fdd24c;
    --brand-blue: #0059b3;
    --tile-top: #ffffff;
    --tile-bottom: #e3eef5;
  }
  * { margin: 0; padding: 0; box-sizing: border-box; }
  html, body { width: 927px; height: 1200px; overflow: hidden; background: var(--page); }
  .poster { position: relative; width: 927px; height: 1200px; }
  .panel {
    position: absolute; left: 23px; top: 26px; width: 878px; height: 1146px;
    background: var(--panel-green); border-radius: 33px;
  }
  .stop-sign { position: absolute; top: 58px; width: 218px; height: 218px; }
  .stop-sign--left { left: 41px; }
  .stop-sign--right { left: 668px; }
  .stop-sign text {
    font-family: "Arimo", Arial, sans-serif; font-weight: 700; font-size: 64px; fill: var(--white);
  }
  .title, .call-out, .instruction, .choice-word {
    position: absolute; left: 0; width: 927px; text-align: center;
    font-family: "Fira Sans Extra Condensed", "Arial Narrow", sans-serif;
  }
  .title {
    top: 110px; color: var(--white); font-weight: 600; font-size: 72px; line-height: 63px;
    letter-spacing: -1px;
  }
  .call-out {
    top: 280px; color: var(--headline-yellow); font-weight: 700; font-size: 74px; line-height: 76px;
    letter-spacing: -0.5px;
  }
  .instruction {
    color: var(--white); font-weight: 600; font-size: 39px; line-height: 51px; letter-spacing: -0.3px;
  }
  .instruction--hands { top: 356px; }
  .instruction--cover { top: 692px; }
  .tile {
    position: absolute; border-radius: 25px;
    background: linear-gradient(180deg, var(--tile-top) 0%, var(--tile-bottom) 100%);
  }
  .tile--sanitizer { left: 371px; top: 480px; width: 201px; height: 203px; }
  .tile--face-shield { left: 233px; top: 816px; width: 202px; height: 203px; }
  .tile--goggles { left: 514px; top: 816px; width: 202px; height: 203px; }
  .choice-word { top: 874px; color: var(--white); font-weight: 600; font-size: 50px; line-height: 60px; }
  .brand-mark {
    position: absolute; left: 540px; top: 1056px; width: 159px; height: 91px;
    display: flex; align-items: center; gap: 10px;
  }
  .brand-mark__square { width: 48px; height: 48px; background: var(--brand-blue); flex: none; }
  .brand-mark__name {
    font-family: "Nunito Sans", Arial, sans-serif; font-weight: 800; font-size: 30px; line-height: 1;
    color: var(--white);
  }
  .agency {
    position: absolute; left: 712px; top: 1071px; color: var(--white);
    font-family: "Nunito Sans", Arial, sans-serif; font-size: 12px; line-height: 15px;
    white-space: nowrap;
  }
  .agency strong { font-weight: 800; display: block; }
  .agency span { font-weight: 400; display: block; }
  .form-code {
    position: absolute; left: 36px; top: 1030px; transform: rotate(90deg); transform-origin: left top;
    font-family: "Nunito Sans", Arial, sans-serif; font-size: 8px; color: var(--white);
    white-space: nowrap;
  }
</style>
</head>
<body>
<main class="poster">
  <div class="panel"></div>

  <svg class="stop-sign stop-sign--left" viewBox="0 0 218 218" aria-hidden="true">
    <polygon points="64,0 154,0 218,64 218,154 154,218 64,218 0,154 0,64" fill="#ffffff"/>
    <polygon points="66,5 152,5 213,66 213,152 152,213 66,213 5,152 5,66" fill="var(--stop-red)"/>
    <polygon points="70,14 148,14 204,70 204,148 148,204 70,204 14,148 14,70" fill="none" stroke="#ffffff" stroke-width="2.5"/>
    <text x="109" y="133" text-anchor="middle">STOP</text>
  </svg>
  <svg class="stop-sign stop-sign--right" viewBox="0 0 218 218" aria-hidden="true">
    <polygon points="64,0 154,0 218,64 218,154 154,218 64,218 0,154 0,64" fill="#ffffff"/>
    <polygon points="66,5 152,5 213,66 213,152 152,213 66,213 5,152 5,66" fill="var(--stop-red)"/>
    <polygon points="70,14 148,14 204,70 204,148 148,204 70,204 14,148 14,70" fill="none" stroke="#ffffff" stroke-width="2.5"/>
    <text x="109" y="133" text-anchor="middle">STOP</text>
  </svg>

  <h1 class="title">DROPLET<br>PRECAUTIONS</h1>
  <h2 class="call-out">EVERYONE MUST:</h2>

  <p class="instruction instruction--hands">Clean their hands, including before<br>entering and when leaving the room.</p>
  <div class="tile tile--sanitizer" role="img" aria-label="Hand receiving a drop of alcohol-based hand rub from a pump bottle"></div>

  <p class="instruction instruction--cover">Make sure their eyes, nose and mouth are<br>fully covered before room entry.</p>
  <div class="tile tile--face-shield" role="img" aria-label="Health worker wearing a face shield and a surgical mask"></div>
  <p class="choice-word">or</p>
  <div class="tile tile--goggles" role="img" aria-label="Health worker wearing goggles and a surgical mask"></div>

  <div class="brand-mark">
    <div class="brand-mark__square"></div>
    <span class="brand-mark__name">PWR</span>
  </div>
  <p class="agency">
    <strong>Regional Office of</strong>
    <strong>Public Wellness Resources</strong>
    <span>Center for Community</span>
    <span>Health and Prevention</span>
  </p>

  <p class="form-code">CS19-306149-A</p>
</main>
</body>
</html>
```